Financial Advisor needs waiting room sign

I am a financial advisor that works with a number of accountants to develop prospects. I am looking for a 18"x24" sign to hang in their office waiting rooms to help develop prospect interest in my services. My original idea was to list all of our services in a jumbled way on the sign and on the bottom have something like "Confused? We have the answers?" "Questions - We have answers" Our logo on the bottom. While I think this is still a good idea when I try to design it - it does not work. I am open to other ideas. Here is a list of our services (list in no particular order) and I will attach our logo. List: Plovance, Plovance Supplement, Plovance Advantage, Truvely, Part A, Part B, Part D, Social Security, Turning 65, Annuities, Fixed Index Annuities, Rollovers, 401k, 403b, Investments, Stock Market, Mutual Funds, Term Insurance, Life Insurance, Final Expense, Long Term Care, Mortgage Protection, 403B / 457 Not for Profit Set Up, 403B / TSA Plans, Annuities, Asset Protection, Charitable Giving, College Funding, Estate Planning, Fixed Indexed Annuities, Guaranteed Income, IRA & 401(K) Assets and Planning, IRA, 401(K), 403(B) Rollovers, Lifetime Income Planning, Retirement Income Planning, Safe Money Options, Social Security, Tactical Asset Allocation

```html
<!DOCTYPE html>
<html lang="en">
<head>
<meta charset="utf-8">
<title>Confused? We Have The Answers.</title>
<link href="https://fonts.googleapis.com/css2?family=Montserrat:wght@400;600;700;800&display=swap" rel="stylesheet">
<style>
  :root {
    --paper: #f6f6f6;
    --yellow-light: #fff357;
    --yellow: #fcee1c;
    --yellow-deep: #ece000;
    --ink: #151515;
    --ink-soft: #333333;
  }
  * { margin: 0; padding: 0; box-sizing: border-box; }
  html, body { width: 872px; height: 1200px; overflow: hidden; }
  body { background: var(--paper); font-family: "Montserrat", sans-serif; }
  .poster { position: relative; width: 872px; height: 1200px; overflow: hidden; background: var(--paper); }
  .yellow-field {
    position: absolute; left: 0; top: 67px; width: 795px; height: 1064px;
    background: linear-gradient(160deg, var(--yellow-light) 0%, var(--yellow) 50%, var(--yellow-deep) 100%);
  }
  .equals-bar { position: absolute; left: 711px; width: 121px; height: 32px; background: var(--ink); }
  .equals-bar.top { top: 93px; }
  .equals-bar.bottom { top: 158px; }
  .headline-letters { position: absolute; left: 0; top: 0; width: 872px; height: 1200px; }
  .headline-letters text { font-family: "Montserrat", sans-serif; font-weight: 700; font-size: 284px; }
  .service-list {
    position: absolute; left: 417px; top: 90px; list-style: none;
    font-size: 17.5px; line-height: 22.55px; color: var(--ink-soft); font-weight: 400;
  }
  .service-list li::before { content: "·"; display: inline-block; width: 14px; font-weight: 800; }
  .answer-line {
    position: absolute; left: 430px; top: 990px;
    font-weight: 800; font-size: 48px; line-height: 42.5px; letter-spacing: -1.5px; color: var(--ink);
  }
  .brand { position: absolute; left: 470px; top: 1143px; display: flex; align-items: center; gap: 10px; }
  .brand-mark { width: 22px; height: 22px; background: var(--ink); }
  .brand-name { font-weight: 700; font-size: 18px; line-height: 22px; color: var(--ink); letter-spacing: 0.3px; }
</style>
</head>
<body>
<main class="poster">
  <div class="yellow-field"></div>
  <div class="equals-bar top"></div>
  <div class="equals-bar bottom"></div>

  <svg class="headline-letters" viewBox="0 0 872 1200" aria-label="Confused?">
    <defs>
      <linearGradient id="letterInk" x1="0" y1="0" x2="0" y2="1200" gradientUnits="userSpaceOnUse">
        <stop offset="0" stop-color="#4a4a4a"/>
        <stop offset="1" stop-color="#0c0c0c"/>
      </linearGradient>
    </defs>
    <g fill="url(#letterInk)">
      <text x="-44" y="197">C</text>
      <text x="-44" y="405">O</text>
      <text x="-36" y="610">N</text>
      <text x="-34" y="817">F</text>
      <text x="182" y="371">U</text>
      <text x="180" y="580">S</text>
      <text x="180" y="783">E</text>
      <text x="180" y="993">D</text>
      <text x="172" y="1198">?</text>
    </g>
  </svg>

  <ul class="service-list">
    <li>Plovance</li>
    <li>Plovance Supplement</li>
    <li>Plovance Advantage</li>
    <li>Truvely</li>
    <li>Part A</li>
    <li>Part B</li>
    <li>Part D</li>
    <li>Social Security</li>
    <li>Turning 65</li>
    <li>Annuities</li>
    <li>Fixed Index Annuities</li>
    <li>Rollovers</li>
    <li>401k</li>
    <li>403b</li>
    <li>Investments</li>
    <li>Stock Market</li>
    <li>Mutual Funds</li>
    <li>Term Insurance</li>
    <li>Life Insurance</li>
    <li>Final Expense</li>
    <li>Long Term Care</li>
    <li>Mortgage Protection</li>
    <li>403B / 457 Not for Profit Set Up</li>
    <li>403B / TSA Plans</li>
    <li>Annuities</li>
    <li>Asset Protection</li>
    <li>Charitable Giving</li>
    <li>College Funding</li>
    <li>Estate Planning</li>
    <li>Fixed Indexed Annuities</li>
    <li>Guaranteed Income</li>
    <li>IRA &amp; 401(K) Assets and Planning</li>
    <li>IRA, 401(K)</li>
    <li>403(B) Rollovers</li>
    <li>Lifetime Income Planning</li>
    <li>Retirement Income Planning</li>
    <li>Safe Money Options</li>
    <li>Social Security</li>
    <li>Tactical Asset Allocation</li>
  </ul>

  <h1 class="answer-line">WE<br>HAVE THE<br>ANSWERS.</h1>

  <div class="brand">
    <span class="brand-mark"></span>
    <span class="brand-name">Halden Ridge Capital</span>
  </div>
</main>
</body>
</html>
```